Lifestyle management firm needs PDF/brochure created from existing web content for InDesign

We are a boutique lifestyle management company based in NY with offices in San Francisco. We looking to create a brochure directed towards larger corporate partners and developers. We have already created the web content for this branch of our business. We would like to create a PDF presentation of the web content that we can use for in person presentations and to email to potential partners and clients. It should be a basic brochure version of the web content. The website is on sitebloc.net and we need to take that design and recreate it in in Illustrator or In Design so that it can ultimately be saved as a PDF and emailed or handed out as a presentation.

See www.harborlanestewards.com

Thank you,

Marnie

Target Market(s)

Real estate developers and corporate partners

Industry/Entity Type

Boutique

Requirements
Must have
• Should be based on the existing web content. Should be easy to email. Should be created in InDesign or illustrator.
Nice to have
• An easy to print format so we have the option to present it in person.

```html
<!DOCTYPE html>
<html lang="en">
<head>
<meta charset="utf-8">
<title>Harborlane – Amenity Services Brochure</title>
<link rel="stylesheet" href="https://fonts.googleapis.com/css2?family=Open+Sans:wght@400;600&family=Noto+Serif:wght@400&display=swap">
<style>
  :root {
    --backdrop: #e4e5e6;
    --paper: #ffffff;
    --aqua: #9fd8dc;
    --brand-brown: #4b3f3e;
    --heading: #1f1f1f;
    --body-text: #6b6b6b;
    --photo-fill: #b4bcb2;
  }
  * { box-sizing: border-box; margin: 0; padding: 0; }
  html, body {
    width: 1200px; height: 846px; overflow: hidden;
    background: var(--backdrop);
  }
  .canvas { position: relative; width: 1200px; height: 846px; }

  .page {
    position: absolute;
    width: 458px; height: 647px;
    background: var(--paper);
  }
  .page--amenities { left: 92px; top: 91px; }
  .page--onsite { left: 628px; top: 105px; }

  .band { position: absolute; left: 0; width: 100%; height: 15px; background: var(--aqua); }
  .band--top { top: 0; }
  .band--bottom { bottom: 0; }

  .wordmark {
    position: absolute; left: 0; right: 0; top: 28px;
    text-align: center;
    font-family: "Open Sans", sans-serif;
    font-weight: 400;
    font-size: 64px; line-height: 1;
    letter-spacing: -1px;
    color: var(--brand-brown);
  }
  .tagline {
    position: absolute; left: 0; right: 0; top: 104px;
    text-align: center;
    font-family: "Open Sans", sans-serif;
    font-size: 16px; letter-spacing: 0.6px;
    color: var(--brand-brown);
  }
  .rule {
    position: absolute; left: 15px; right: 17px;
    height: 2px; background: var(--aqua);
  }
  .rule--head { top: 136px; }

  .section-title {
    position: absolute; left: 0; right: 0; top: 157px;
    text-align: center;
    font-family: "Open Sans", sans-serif;
    font-weight: 600; font-size: 18px; letter-spacing: 1.6px;
    color: var(--heading);
  }
  .title-underline {
    position: absolute; top: 191px; left: 121px; width: 215px;
    height: 2px; background: var(--aqua);
  }

  .intro {
    position: absolute; left: 30px; right: 30px; top: 196px;
    text-align: center;
    font-family: "Noto Serif", serif;
    font-size: 11px; line-height: 14.5px;
    color: var(--body-text);
  }
  .page--onsite .intro { top: 218px; left: 44px; right: 44px; }

  .offering {
    position: absolute; left: 0; right: 0;
    text-align: center;
    font-family: "Open Sans", sans-serif;
    font-weight: 600; font-size: 13px; line-height: 17px; letter-spacing: 1.2px;
    color: var(--heading);
  }

  .duties {
    position: absolute; left: 39px; top: 297px;
    list-style: none;
    font-family: "Noto Serif", serif;
    font-size: 11px; line-height: 19.6px;
    color: var(--body-text);
  }
  .duties li::before {
    content: ""; display: inline-block;
    width: 5px; height: 5px; border-radius: 50%;
    background: var(--heading);
    margin-right: 5px; vertical-align: 2px;
  }

  .photo-slot {
    position: absolute; left: 16px; right: 16px;
    height: 103px;
    background: var(--photo-fill);
  }
  .page--amenities .photo-slot { top: 493px; }
  .page--onsite .photo-slot { top: 482px; }

  .contact {
    position: absolute; left: 16px; right: 16px; top: 613px;
    display: flex; justify-content: space-between;
    font-family: "Noto Serif", serif;
    font-size: 11.5px;
    color: var(--body-text);
  }
</style>
</head>
<body>
<main class="canvas">

  <section class="page page--amenities">
    <div class="band band--top"></div>
    <div class="wordmark">harborlane</div>
    <div class="tagline">solutions for an organized urban lifestyle</div>
    <div class="rule rule--head"></div>

    <h1 class="section-title">HARBORLANE AMENITY SERVICES</h1>
    <p class="intro">We believe Harborlane's core values and standards of excellence are the perfect compliment to a distinguished luxury residence.<br>The following comprise our amenity offerings and can be customed<br>tailored to meet the needs of individual buildings.</p>

    <h2 class="offering" style="top:279px">HARBORLANE ON-SITE</h2>
    <div class="rule" style="top:313px"></div>
    <h2 class="offering" style="top:333px">ON-CALL PERSONAL ASSISTANTS</h2>
    <div class="rule" style="top:367px"></div>
    <h2 class="offering" style="top:387px">HARBORLANE CONCIERGE</h2>
    <div class="rule" style="top:421px"></div>
    <h2 class="offering" style="top:441px">UNIQIE PROGRAMMING<br>&amp; EXPERIENCES</h2>

    <div class="photo-slot" role="img" aria-label="Panoramic window view over a city park and skyline"></div>

    <footer class="contact">
      <span>info@harborlanenyc.com</span>
      <span>212.555.0148</span>
      <span>www.harborlanenyc.com</span>
    </footer>
    <div class="band band--bottom"></div>
  </section>

  <section class="page page--onsite">
    <div class="band band--top"></div>
    <div class="wordmark">harborlane</div>
    <div class="tagline">solutions for an organized urban lifestyle</div>
    <div class="rule rule--head"></div>

    <h1 class="section-title">HARBORLANE ON-SITE</h1>
    <div class="title-underline"></div>
    <p class="intro">The dedicated on-site manager is the face of Harborlane.&nbsp; This is the<br>point person who is available Monday through Friday<br>from either 8am-5pm or 9am-6pm to:</p>

    <ul class="duties">
      <li>Facilitate all resident requests (virtual and otherwise)</li>
      <li>Handle all concierge requests</li>
      <li>Manage the team of on-call personal assistants</li>
      <li>Liaise with our preferred vendors to meet client needs</li>
      <li>Curate unique programming and experiences for residents</li>
    </ul>

    <div class="photo-slot" role="img" aria-label="Panoramic window view over a city park and skyline"></div>

    <footer class="contact">
      <span>info@harborlanenyc.com</span>
      <span>212.555.0148</span>
      <span>www.harborlanenyc.com</span>
    </footer>
    <div class="band band--bottom"></div>
  </section>

</main>
</body>
</html>
```